LEARN Business Skills so you can Earn a good living

size of the poster is 8”x 10.75" plus 0.25" bleed.
Please leave 1 inch on the bottoum for footer
I want a design a poster that will attract people's attention.
I appreciate a creative ad however the ad should not take away from being able to clearly read the text.
-I also appreciate a simple creative ad that is not too busy.
-you can use graphics, vectors, or pictures of real people.
-however, if you use real people it should be a white male that is wearing a white shirt and look like a professional person.

Target Market(s)

Potential young business people

Industry/Entity Type

education

Requirements
Must have
• easy to read the text
Nice to have
• I would like a "creative" simple ad that is easy to be read
Should not have
• pictures of women

```html
<!DOCTYPE html>
<html lang="en">
<head>
<meta charset="utf-8">
<title>Learn to Earn – Business Enrichment Course</title>
<link rel="stylesheet" href="https://fonts.googleapis.com/css2?family=Alegreya+Sans:wght@700;800;900&family=Marcellus&family=Oswald:wght@500&family=Crimson+Text&display=swap">
<style>
  :root {
    --navy: #0a4382;
    --band-blue: #1477c0;
    --orange: #f26522;
    --paper: #ffffff;
    --backdrop: #ebe9e6;
    --photo-light: #ece7e2;
    --photo-dark: #c9bfb6;
  }
  * { margin: 0; padding: 0; box-sizing: border-box; }
  html, body { width: 1200px; height: 800px; overflow: hidden; background: var(--backdrop); }
  .poster {
    position: absolute; left: 332px; top: 10px;
    width: 535px; height: 780px;
    background: var(--paper); overflow: hidden;
  }
  .top-band { position: absolute; left: 0; top: 0; width: 100%; height: 16px; background: var(--band-blue); }
  .presenter-photo {
    position: absolute; left: 404px; top: 360px; width: 131px; height: 351px;
    background: linear-gradient(180deg, var(--photo-light) 0%, var(--photo-dark) 100%);
  }
  .course-band { position: absolute; left: 0; top: 269px; width: 100%; height: 49px; background: var(--band-blue); }
  .promise-band { position: absolute; left: 18px; top: 321px; width: 441px; height: 33px; background: var(--orange); }
  .layer { position: absolute; left: 0; top: 0; width: 535px; height: 780px; }
  .word { font-family: "Alegreya Sans", sans-serif; font-weight: 800; fill: var(--navy); }
  .connector { font-family: "Crimson Text", serif; fill: var(--orange); }
  .course-title { font-family: "Alegreya Sans", sans-serif; font-weight: 800; fill: var(--paper); }
  .promise { font-family: "Oswald", sans-serif; font-weight: 500; fill: var(--paper); }
  .skills-title { font-family: "Alegreya Sans", sans-serif; font-weight: 800; fill: var(--navy); }
  .goal { font-family: "Oswald", sans-serif; font-weight: 500; fill: var(--orange); }
  .rule { position: absolute; left: 0; height: 2px; background: var(--navy); }
  .rule.under-title { top: 444px; width: 404px; }
  .rule.under-goals { top: 495px; width: 333px; }
  .rule.bottom { top: 711px; width: 100%; }
  .topics {
    position: absolute; top: 506px; list-style: none;
    font-family: "Marcellus", serif; font-size: 12px; line-height: 17.1px;
    color: var(--navy);
  }
  .topics.first { left: 38px; }
  .topics.second { left: 190px; top: 540.2px; }
  .topics li { position: relative; padding-left: 11px; white-space: nowrap; }
  .topics li::before {
    content: ""; position: absolute; left: 0; top: 3px;
    width: 6px; height: 6px; border-radius: 50%; background: var(--orange);
  }
</style>
</head>
<body>
  <main class="poster">
    <div class="top-band"></div>
    <div class="presenter-photo" role="img" aria-label="Photo of a smiling young professional man in a white shirt pointing up toward the text"></div>
    <div class="course-band"></div>
    <div class="promise-band"></div>

    <svg class="layer" viewBox="0 0 535 780">
      <g aria-label="Learn to Earn">
        <text class="word" x="48" y="135" font-size="150" textLength="437" lengthAdjust="spacingAndGlyphs">LEARN</text>
        <text class="connector" x="54" y="187" font-size="52" textLength="43" lengthAdjust="spacingAndGlyphs">to</text>
        <text class="word" x="114" y="260" font-size="154" textLength="373" lengthAdjust="spacingAndGlyphs">EARN</text>
      </g>
      <text class="course-title" x="31" y="306" font-size="38" textLength="461" lengthAdjust="spacingAndGlyphs">Business Enrichment Course</text>
      <text class="promise" x="40" y="345" font-size="21" textLength="398" lengthAdjust="spacingAndGlyphs">A PROVEN SUCCESS OF HELPING PEOPLE IN THEIR LIVELIHOODS</text>
      <text class="skills-title" x="35" y="390" font-size="44" textLength="349" lengthAdjust="spacingAndGlyphs">Business skills that</text>
      <text class="skills-title" x="34" y="431" font-size="44" textLength="253" lengthAdjust="spacingAndGlyphs">will help you:</text>
      <text class="goal" x="33" y="483" font-size="25" textLength="136" lengthAdjust="spacingAndGlyphs">GET A QUALITY JOB</text>
      <text class="goal" x="174" y="469" font-size="19" textLength="181" lengthAdjust="spacingAndGlyphs">- START/GROW YOUR BUSINESS</text>
      <text class="goal" x="174" y="491" font-size="19" textLength="157" lengthAdjust="spacingAndGlyphs">- INCREASE YOUR SALARY</text>
    </svg>

    <div class="rule under-title"></div>
    <div class="rule under-goals"></div>

    <ul class="topics first">
      <li>BUSINESS ADMIISTRATION</li>
      <li>SMALL BUSINESS MANAGEMENT</li>
      <li>FINANCE</li>
      <li>COMPUTERS</li>
      <li>SALES &nbsp;MARKETING</li>
      <li>INTERVIEWING SKILLS</li>
      <li>NEGOTIATION</li>
      <li>IMPORT/EXPORT</li>
      <li>DISTRIBUTION</li>
      <li>LEDGERWISE</li>
      <li>HEALTH CARE</li>
      <li>MARKETVALE</li>
    </ul>
    <ul class="topics second">
      <li>INVESTMENTS</li>
      <li>ACCOUNTING</li>
      <li>PROJECT MANAGEMENT</li>
      <li>BUSINESS LAW</li>
      <li>PUBLIC SPEAKING</li>
      <li>INFORMATION TECHNOLOY</li>
      <li>MARKETING</li>
      <li>REAL ESTATE</li>
      <li>MANAGEMENT</li>
    </ul>

    <div class="rule bottom"></div>
  </main>
</body>
</html>
```